Design a web site for my business - Brellan Coatworks Mackaby.

We are a family business that handles design, fabrication and installation of powder coated aluminum, stainless steel and glass products. Including handrails, privacy slat screens, electric gates and pool fencing. We are based in the Whitsundays in North Queensland and service an area from Airlie Beach to Townsville.

Target Market(s)

Domestic and commercial

Industry/Entity Type

fabrication - manufacturing

Coding

Coded - Design and coding required

Number of Pages Required

5+ page

Colors
0054AA
0677BA
7BADD7
CADEEF
E8F1F8

Requirements
Must have
• photo galleries, contact page, one page for privacy screens, balustrades, glass fencing, stainless steel handrail, powder coated aluminium handrails and pool fencing

```html
<!DOCTYPE html>
<html lang="en">
<head>
<meta charset="utf-8">
<title>About Us – Brellan Coatworks Mackaby</title>
<link rel="stylesheet" href="https://fonts.googleapis.com/css2?family=Outfit:wght@300;400;500;600;700&display=swap">
<style>
:root{
  --blue:#0054AA;
  --blue-mid:#0677BA;
  --blue-soft:#7BADD7;
  --blue-pale:#CADEEF;
  --blue-mist:#E8F1F8;
  --page:#F2F6FB;
  --ink:#111418;
  --text:#23272d;
  --muted:#5d636b;
  --navy:#062B62;
  --white:#ffffff;
}
*{box-sizing:border-box;margin:0;padding:0}
html,body{width:1200px;height:3651px;overflow:hidden}
body{background:var(--page);font-family:"Outfit",Arial,sans-serif;color:var(--text);position:relative}
.abs{position:absolute}
h1,h2,h3{font-weight:700;color:var(--ink);text-transform:uppercase;letter-spacing:-0.5px}

/* header */
.site-header{position:absolute;left:0;top:0;width:1200px;height:82px;background:var(--page)}
.brand{position:absolute;left:67px;top:22px;display:flex;align-items:center;gap:8px}
.brand-mark{width:24px;height:24px;border-radius:50%;background:var(--ink)}
.brand-name{font-size:11px;font-weight:600;color:var(--ink);line-height:1.2;width:90px}
.main-nav{position:absolute;right:67px;top:0;height:82px;display:flex;gap:38px}
.main-nav a{font-size:14px;color:#444;text-decoration:none;line-height:84px;position:relative}
.main-nav a.active{color:var(--ink);font-weight:600}
.main-nav a.active::after{content:"";position:absolute;left:-3px;right:-3px;bottom:0;height:3px;background:#3a4150}

/* hero */
.hero{position:absolute;left:0;top:82px;width:1200px;height:518px;
  background:linear-gradient(180deg,#2f3e4c 0%,#6b8197 35%,#9db6cf 60%,#55687a 100%)}
.hero-title{position:absolute;top:230px;width:1200px;text-align:center;color:var(--white);font-size:66px;line-height:78px;letter-spacing:-1.5px}
.hero-sub{position:absolute;top:402px;left:150px;width:900px;text-align:center;color:var(--white);font-size:18.5px;line-height:25px}

/* common */
.eyebrow{display:flex;align-items:center;gap:16px;font-size:15px;font-weight:500;color:var(--blue)}
.eyebrow::before{content:"";width:50px;height:1.5px;background:var(--blue)}
.section-title{font-size:40px;line-height:46px}
.body-copy{font-size:19px;line-height:25px;color:var(--text)}
.photo{position:absolute}
.btn{position:absolute;height:54px;border-radius:27px;font-size:18.5px;font-weight:500;display:flex;align-items:center;justify-content:center;text-decoration:none}
.btn-primary{background:var(--blue);color:var(--white);box-shadow:0 4px 10px rgba(0,84,170,.3)}
.btn-ghost{background:var(--blue-mist);color:var(--blue);border:1.5px solid var(--blue-pale)}

/* process */
.step{position:absolute;top:1845px;width:240px}
.step-num{width:45px;height:45px;border-radius:50%;border:1.5px dashed var(--blue-soft);color:var(--blue);font-size:15px;display:flex;align-items:center;justify-content:center}
.step h3{text-transform:none;font-size:19px;font-weight:600;margin-top:22px;letter-spacing:0}
.step p{font-size:15.5px;line-height:21px;color:var(--muted);margin-top:9px}

/* areas */
.areas{position:absolute;left:0;top:2123px;width:1200px;height:576px;background:var(--blue-mist)}
.area-card{position:absolute;height:83px;background:#DCE8F4;border:1px solid var(--blue-pale);display:flex;align-items:center;justify-content:space-between;padding:0 30px;font-size:20px;font-weight:500}
.area-card .name{color:var(--ink)}
.area-card .dist{color:var(--blue)}

/* footer */
.site-footer{position:absolute;left:27px;top:3261px;width:1146px;height:361px;background:var(--navy);border-radius:28px;color:#c7d3e6}
.footer-col h4{font-size:18px;font-weight:600;color:var(--white);margin-bottom:17px}
.footer-col li{list-style:none;font-size:15.5px;line-height:28.5px;font-weight:300}
</style>
</head>
<body>

<header class="site-header">
  <div class="brand"><span class="brand-mark"></span><span class="brand-name">BRELLAN COATWORKS MACKABY</span></div>
  <nav class="main-nav">
    <a href="#">Home</a>
    <a href="#" class="active">About Us</a>
    <a href="#">Our Services</a>
    <a href="#">Gallery</a>
    <a href="#">Contact Us</a>
  </nav>
</header>

<section class="hero" role="img" aria-label="Modern multi-storey home with glass balustrades and timber slat screening">
  <h1 class="hero-title">Building Quality That<br>Lasts For Generations</h1>
  <p class="hero-sub">Proudly serving the Whitsundays and North Queensland with premium aluminium, stainless steel, and glass fabrication solutions for residential and commercial projects.</p>
</section>

<!-- our story -->
<div class="eyebrow abs" style="left:67px;top:699px">Our Story</div>
<h2 class="section-title abs" style="left:67px;top:732px">A Family Business Built<br>On Craftsmanship</h2>
<div class="body-copy abs" style="left:67px;top:844px;width:530px">
  <p>Quality workmanship, honest service, and attention to detail have always been at the heart of our business. As a family-owned fabrication company, we combine years of industry experience with modern manufacturing techniques to create products that are both functional and visually striking.</p>
  <p style="margin-top:25px">Every project is carefully designed, fabricated, and installed to meet the unique requirements of our clients. Whether it's a custom handrail, glass balustrade, privacy screen, or automated gate, we are committed to delivering solutions that exceed expectations.</p>
</div>
<div class="photo" role="img" aria-label="Rooftop terrace with frameless glass balustrade and timber bench seating" style="left:609px;top:700px;width:524px;height:442px;background:linear-gradient(160deg,#3f6fa8 0%,#8fb0d3 35%,#d9d5cc 60%,#8b6a4c 100%)"></div>

<!-- mission -->
<div class="photo" role="img" aria-label="Concrete stairs with frameless glass balustrade and louvred aluminium screening" style="left:67px;top:1244px;width:524px;height:293px;background:linear-gradient(135deg,#a9b9c7 0%,#d8e2ea 45%,#b8c3cc 70%,#5f8f3e 100%)"></div>
<h2 class="section-title abs" style="left:626px;top:1262px">Our Mission</h2>
<p class="body-copy abs" style="left:626px;top:1326px;width:510px">To provide premium fabrication solutions that enhance safety, functionality, and architectural appeal while building lasting relationships through exceptional service and quality craftsmanship.</p>
<a class="btn btn-primary" href="#" style="left:626px;top:1467px;width:223px">Request Free Quote</a>
<a class="btn btn-ghost" href="#" style="left:866px;top:1466px;width:169px">View Projects</a>

<!-- process -->
<div class="eyebrow abs" style="left:67px;top:1655px">How We Work</div>
<h2 class="section-title abs" style="left:67px;top:1689px">From First Measure<br>To Final Install</h2>
<p class="body-copy abs" style="right:67px;top:1696px;width:300px;text-align:right">A straightforward four-stage process, the same for every job regardless of size.</p>

<div class="step" style="left:67px"><div class="step-num">01</div><h3>Consultation</h3><p>On-site measure and discussion of materials, finish and budget.</p></div>
<div class="step" style="left:337px"><div class="step-num">02</div><h3>Design</h3><p>Detailed spec drawings and colour/finish selection signed off before fabrication.</p></div>
<div class="step" style="left:608px"><div class="step-num">03</div><h3>Fabrication</h3><p>Precision cut, welded &amp; powder coated in our Whitsundays workshop.</p></div>
<div class="step" style="left:878px"><div class="step-num">04</div><h3>Installation</h3><p>Site install by our own certified team, finished and signed off.</p></div>

<!-- areas -->
<section class="areas">
  <div class="eyebrow abs" style="left:510px;top:67px">Where We Work</div>
  <h2 class="section-title abs" style="left:0;width:1200px;text-align:center;top:100px">Serving North<br>Queensland's Coastline</h2>
  <p class="body-copy abs" style="left:250px;width:700px;text-align:center;top:212px">Based in the Whitsundays, our team travels the coast to fabricate and install on-site — from Bowen down to Townsville.</p>
  <div class="area-card" style="left:67px;top:328px;width:344px"><span class="name">WHITSUNDAYS</span><span class="dist">HQ</span></div>
  <div class="area-card" style="left:428px;top:328px;width:343px"><span class="name">AIRLIE BEACH</span><span class="dist">15 KM</span></div>
  <div class="area-card" style="left:788px;top:328px;width:345px"><span class="name">BOWEN</span><span class="dist">60 KM</span></div>
  <div class="area-card" style="left:248px;top:428px;width:343px"><span class="name">AYR</span><span class="dist">100 KM</span></div>
  <div class="area-card" style="left:608px;top:428px;width:344px"><span class="name">TOWNSVILLE</span><span class="dist">240 KM</span></div>
</section>

<!-- contact cta -->
<div class="eyebrow abs" style="left:523px;top:2817px">Get In Touch</div>
<h2 class="section-title abs" style="left:0;width:1200px;text-align:center;top:2851px">Get In Touch<br>Let's Build Something<br>Exceptional</h2>
<p class="body-copy abs" style="left:340px;width:520px;text-align:center;top:3002px">Tell us about your project and we'll get back to you with a free, no-obligation quote.</p>
<a class="btn btn-primary" href="#" style="left:395px;top:3088px;width:224px">Request Free Quote</a>
<a class="btn btn-ghost" href="#" style="left:635px;top:3088px;width:169px">View Projects</a>

<footer class="site-footer">
  <div class="abs" style="left:67px;top:55px;display:flex;align-items:center;gap:8px">
    <span style="width:24px;height:24px;border-radius:50%;background:var(--white)"></span>
    <span style="font-size:11px;font-weight:600;color:var(--white);width:90px;line-height:1.2">BRELLAN COATWORKS MACKABY</span>
  </div>
  <p class="abs" style="left:67px;top:147px;width:270px;font-size:17px;line-height:27px;font-weight:300">Family-owned fabrication of aluminium and stainless steel handrails, glass.</p>
  <div class="footer-col abs" style="left:429px;top:50px"><h4>SERVICES</h4><ul><li>Glass Balustrades</li><li>Pool Fencing</li><li>Handrails</li><li>Electric Gates</li><li>Slat Screens</li></ul></div>
  <div class="footer-col abs" style="left:623px;top:50px"><h4>COMPANY</h4><ul><li>About Us</li><li>Our Projects</li><li>Request a Quote</li><li>Service Areas</li></ul></div>
  <div class="footer-col abs" style="left:818px;top:50px"><h4>CONTACT</h4><ul><li>0700 000 000</li><li>info@brellancoatworks.com.au</li><li>Mon–Fri: 7am – 4pm</li><li>Sat: By appointment</li></ul></div>
  <p class="abs" style="left:0;width:1146px;text-align:center;top:320px;font-size:15px;font-weight:300">© 2026 Brellan Coatworks Mackaby. All rights reserved</p>
</footer>

</body>
</html>
```